Navelo Partnering Business Card

Hello everyone. We need a business card design that would match our logo and the theme we're trying to have for Navelo that you can find on our website and/or Corvapage page

```html
<!DOCTYPE html>
<html lang="en">
<head>
<meta charset="utf-8">
<title>Navelo Partnering Business Card</title>
<link rel="stylesheet" href="https://fonts.googleapis.com/css2?family=Arimo:wght@400;700&display=swap">
<style>
  :root {
    --navy: #052e5f;
    --navy-soft: #0d3866;
    --teal: #00aca4;
    --gold: #ebb42a;
    --shadow-grey: #d3d3d3;
    --plum: #35205a;
    --ink: #2e2e2e;
    --card-edge: #4a4a4a;
    --paper: #ffffff;
  }
  html, body {
    margin: 0;
    padding: 0;
    width: 955px;
    height: 1200px;
    overflow: hidden;
    background: var(--paper);
    font-family: "Arimo", Arial, sans-serif;
  }
  .canvas { position: relative; width: 955px; height: 1200px; }
  .card {
    position: absolute;
    left: 2px;
    width: 947px;
    height: 583px;
    border: 2px solid var(--card-edge);
    border-radius: 24px;
    overflow: hidden;
    background: var(--paper);
  }
  .card--front { top: 2px; }
  .card--back { top: 604px; height: 590px; }
  .card__art { position: absolute; inset: 0; width: 100%; height: 100%; }

  .brand-name {
    position: absolute;
    left: 130px;
    top: 252px;
    width: 230px;
    text-align: center;
    font-size: 56px;
    font-weight: 700;
    color: var(--plum);
    letter-spacing: -1px;
  }
  .brand-caption {
    position: absolute;
    left: 118px;
    top: 407px;
    font-size: 27px;
    color: var(--navy);
    white-space: nowrap;
  }
  .brand-caption strong { font-weight: 700; }

  .divider {
    position: absolute;
    left: 76px;
    top: 197px;
    width: 380px;
    height: 4px;
    background: var(--teal);
  }
  .contact-list {
    position: absolute;
    left: 105px;
    top: 284px;
    margin: 0;
    padding: 0;
    list-style: none;
  }
  .contact-item {
    display: flex;
    align-items: center;
    height: 40px;
    margin-bottom: 28px;
    font-size: 32px;
    color: var(--ink);
  }
  .contact-item svg { width: 34px; height: 34px; margin-right: 28px; flex: none; }
</style>
</head>
<body>
<div class="canvas">

  <section class="card card--front">
    <svg class="card__art" viewBox="0 0 1050 648" preserveAspectRatio="none" aria-hidden="true">
      <defs>
        <linearGradient id="wave-band-front" x1="0" y1="0" x2="1" y2="0">
          <stop offset="0" stop-color="#0d3866"/>
          <stop offset="0.3" stop-color="#2f6f8a"/>
          <stop offset="0.55" stop-color="#c9d3dc"/>
          <stop offset="0.8" stop-color="#ebb42a"/>
          <stop offset="1" stop-color="#f0c857"/>
        </linearGradient>
      </defs>
      <polygon points="303,0 335,0 645,648 612,648" fill="var(--shadow-grey)"/>
      <polygon points="330,0 455,0 770,648 640,648" fill="var(--teal)"/>
      <polygon points="455,0 1050,0 1050,648 770,648" fill="var(--navy)"/>
      <polygon points="455,0 1050,0 1050,74 490,74" fill="url(#wave-band-front)"
               role="img" aria-label="Decorative band of flowing gold, white and teal lines"/>
      <polygon points="490,74 1045,74 1045,94 500,94" fill="var(--gold)"/>
      <polygon points="500,94 1045,94 1045,98 502,98" fill="var(--paper)"/>
    </svg>
    <div class="brand-name">Navelo</div>
    <div class="brand-caption"><strong>Navelo</strong> PARTNERING</div>
  </section>

  <section class="card card--back">
    <svg class="card__art" viewBox="0 0 1050 655" preserveAspectRatio="none" aria-hidden="true">
      <defs>
        <linearGradient id="wave-band-back" x1="0" y1="0" x2="1" y2="1">
          <stop offset="0" stop-color="#0d3866" stop-opacity="0"/>
          <stop offset="0.35" stop-color="#ebb42a" stop-opacity="0.35"/>
          <stop offset="0.7" stop-color="#00aca4" stop-opacity="0.3"/>
          <stop offset="1" stop-color="#052e5f" stop-opacity="0"/>
        </linearGradient>
      </defs>
      <polygon points="0,355 0,655 230,655" fill="var(--teal)"/>
      <polygon points="430,0 470,0 790,655 750,655" fill="var(--shadow-grey)"/>
      <polygon points="470,0 683,0 765,178 1050,178 1050,655 785,655" fill="var(--navy-soft)"/>
      <polygon points="535,136 1050,178 1050,655 785,655" fill="var(--navy)"/>
      <polygon points="535,136 640,136 1050,420 1050,655 785,655" fill="url(#wave-band-back)"
               role="img" aria-label="Decorative sweep of flowing gold, white and teal lines"/>
      <polygon points="607,488 607,655 690,655" fill="var(--gold)"/>
    </svg>
    <div class="divider"></div>
    <ul class="contact-list">
      <li class="contact-item">
        <svg viewBox="0 0 34 34" aria-hidden="true">
          <circle cx="17" cy="17" r="15.5" fill="none" stroke="#111" stroke-width="1.6"/>
          <path d="M11.5 10.5c1-1 2-1 2.6 0l1.3 2.3c.4.8.2 1.5-.5 2l-.9.6c.8 1.9 2.2 3.4 4.1 4.3l.6-.9c.5-.7 1.2-.9 2-.5l2.3 1.3c1 .6 1 1.6 0 2.6-1.2 1.3-3 1.6-5 .6-3.2-1.6-5.6-4-7-7.2-.9-2-.6-3.8.5-5.1z" fill="#111"/>
        </svg>
        Phone
      </li>
      <li class="contact-item">
        <svg viewBox="0 0 34 34" aria-hidden="true">
          <rect x="1" y="6" width="32" height="22" fill="#111"/>
          <path d="M2 7l15 12L32 7M2 27l11-10M32 27L21 17" fill="none" stroke="#fff" stroke-width="1.8"/>
        </svg>
        Email
      </li>
      <li class="contact-item">
        <svg viewBox="0 0 34 34" aria-hidden="true" fill="none" stroke="#111" stroke-width="1.5">
          <circle cx="17" cy="17" r="15"/>
          <ellipse cx="17" cy="17" rx="7" ry="15"/>
          <path d="M17 2v30M2 17h30M4.5 9.5h25M4.5 24.5h25"/>
        </svg>
        Website
      </li>
    </ul>
  </section>

</div>
</body>
</html>
```